Online Trading Web-Design

Web design is required for a new startup that specialises in online trading between buyers and sellers of fashion apparel. The company is called: Bright Cove Hub (bch)

Website needs to be clean and css friendly. we like the idea of having a largish "banner" on the homepage which we can rotate using HTML5. examples of the banners are: http://au.plevrix.com/ ; http://www.dorvanqe.com.au/

the logo has been established already, please limit designs around the colors already established (see uploaded logo).
Updates

Hi, a few clarifications:

1. although the website deals in online trading for clothes etc. the main focus of the website needs to be about highlighting trading between buyers (clothing stores) and sellers (clothing brands). so the website wont be directly selling items of clothes etc.

Industry/Entity Type

Fashion

```html
<!DOCTYPE html>
<html lang="en">
<head>
<meta charset="utf-8">
<title>Bright Cove Hub (bch)</title>
<link rel="stylesheet" href="https://fonts.googleapis.com/css2?family=Open+Sans:ital,wght@0,400;0,600;1,400&display=swap">
<style>
:root{
  --page:#f3f3f3;
  --sky:#86b9e6;
  --sky-dark:#6fa6d8;
  --blue:#2a78c4;
  --link:#2f86d1;
  --ink:#1b1b1b;
  --muted:#555;
  --grey:#e2e2e2;
  --line:#c9c9c9;
  --card-border:#a9cdeb;
  --footer:#3e3f43;
  --footer-bottom:#2a2a2b;
  --teal:#62c7cf;
  --suit-grey:#8d8d8d;
  --suit-stone:#bdb6a8;
  --suit-check:#6f8596;
  --suit-peach:#e6c3aa;
}
*{box-sizing:border-box;margin:0;padding:0}
html,body{width:900px;height:1200px;overflow:hidden}
body{background:var(--page);font-family:"Open Sans",Arial,sans-serif;color:var(--ink);position:relative}
.abs{position:absolute}
.top-rule{left:0;top:0;width:900px;height:2px;background:var(--sky)}
.brand{left:60px;top:12px;width:244px;height:40px;background:#fff;display:flex;align-items:center;gap:8px;padding-left:12px}
.brand-mark{width:14px;height:14px;border-radius:50%;background:var(--teal)}
.brand-name{font-size:17px;font-weight:600;color:var(--teal)}
.cart{left:659px;top:19px;width:179px;height:14px;background:var(--grey);font-size:8px;color:#777;display:flex;align-items:center;justify-content:center;gap:4px}
.account{left:659px;top:41px;width:179px;height:12px;background:#000;color:#fff;font-size:8px;font-weight:600;text-align:center;line-height:12px}
.nav{left:0;top:62px;width:900px;height:22px;background:var(--sky)}
.nav-item{position:absolute;top:0;height:22px;line-height:22px;color:#fff;font-size:9px;padding:0 12px}
.nav-item.active{background:var(--sky-dark)}
.search{left:639px;top:67px;width:137px;height:12px;background:#fff;font-size:8px;color:#aaa;padding-left:3px;line-height:12px}
.submit{left:778px;top:67px;width:60px;height:12px;background:#dedede;font-size:8px;color:#fff;text-align:center;line-height:12px}
.slider{left:60px;top:93px;width:778px;height:139px;border:1px solid var(--card-border);background:#fff;overflow:hidden}
.slide-photo{position:absolute;left:0;top:0;width:100%;height:100%;background:linear-gradient(90deg,#fff 14%,#b8b2a8 24%,#a7a196 50%,#b8b2a8 76%,#fff 86%)}
.slide-caption{position:absolute;left:0;bottom:0;width:100%;height:40px;background:rgba(40,40,40,.9);color:#fff;font-size:8px;padding:5px 12px;line-height:10px}
.arrow{position:absolute;width:34px;height:18px;border-radius:50%;background:#555;border:1px solid #aaa;display:flex;align-items:center;justify-content:center}
.dot{position:absolute;width:6px;height:6px;border-radius:50%;background:var(--sky)}
.hello{left:60px;top:246px;width:778px;height:104px;background:#ececec;border:2px solid #cfcfcf;text-align:center;padding-top:12px}
.hello h1{font-size:14px;font-weight:400;letter-spacing:.3px}
.hello p{font-size:14px;font-style:italic;width:700px;margin:0 auto;line-height:17px}
.hello .cta{display:inline-block;margin-top:12px;width:175px;height:26px;line-height:26px;background:var(--blue);color:#fff;font-size:10px}
.section-title{left:60px;width:778px;height:16px;font-size:15px;display:flex;align-items:center;gap:6px;border-bottom:1px solid var(--line);padding-bottom:4px;height:20px}
.card{width:247px;background:#fff;border:1px solid var(--card-border)}
.card .photo{margin:2px auto 0;width:150px}
.card-title{display:flex;justify-content:space-between;align-items:center;padding:0 12px;color:var(--link);font-size:15px;letter-spacing:.3px}
.count{display:flex;align-items:center;gap:3px}
.btn-detail{margin:0 12px;height:13px;background:var(--grey);color:#999;font-size:8px;text-align:center;line-height:13px}
.btn-cart{margin:2px 12px 0;height:12px;background:var(--blue);color:#fff;font-size:8px;text-align:center;line-height:12px}
.meta{font-size:8px;font-style:italic;color:#444;padding:0 12px;display:flex;align-items:center;gap:4px}
.tile{top:634px;width:179px;height:117px;background:#fff}
.tile .photo{margin:0 auto;width:120px;height:97px}
.tile-label{height:20px;background:var(--grey);color:var(--link);font-size:8px;text-align:center;line-height:20px}
.blog-text{font-size:8px;color:#333;padding:0 17px;line-height:8px}
.blog-meta{font-size:8px;font-style:italic;color:var(--link);padding:0 17px;line-height:9px}
.footer{left:0;top:1028px;width:900px;height:148px;background:var(--footer);border-top:3px solid var(--sky)}
.footer h2{position:absolute;top:10px;font-size:15px;font-weight:400;color:#fff;border-bottom:1px solid #bbb;padding-bottom:4px;width:245px}
.about{position:absolute;left:60px;top:42px;width:230px;font-size:8px;color:#fff;line-height:9.5px}
.random{position:absolute;left:325px;width:245px}
.random .thumb{position:absolute;left:0;width:78px;height:44px;background:#fff;padding:2px 14px}
.random .thumb div{width:100%;height:100%}
.random .name{position:absolute;left:82px;font-size:8px;color:var(--link)}
.random .price{position:absolute;left:82px;width:46px;height:12px;background:var(--blue);color:#fff;font-size:8px;text-align:center;line-height:12px}
.tags{position:absolute;left:591px;top:42px;width:245px;display:flex;flex-wrap:wrap;gap:3px 4px}
.tag{background:#dcdcdc;color:#666;font-size:8px;padding:0 7px;height:12px;line-height:12px}
.bottom-bar{left:0;top:1176px;width:900px;height:24px;background:var(--footer-bottom);font-size:8px;color:#444;padding:8px 60px}
.bottom-bar span{color:var(--link)}
.social{position:absolute;right:62px;top:7px;display:flex;gap:6px}
.social i{width:11px;height:11px;border-radius:50%;background:var(--link);display:block}
</style>
</head>
<body>
<div class="abs top-rule"></div>

<header>
  <div class="abs brand"><span class="brand-mark"></span><span class="brand-name">Bright Cove Hub</span></div>
  <div class="abs cart">
    <svg width="9" height="8" viewBox="0 0 9 8"><path d="M0 1h2l1 4h5l1-3H2.5" fill="none" stroke="#777" stroke-width="1"/><circle cx="3.5" cy="7" r=".8" fill="#777"/><circle cx="7" cy="7" r=".8" fill="#777"/></svg>
    0 item $0
  </div>
  <div class="abs account">LOGIN or REGISTER</div>
  <nav class="abs nav">
    <span class="nav-item active" style="left:60px">Home</span>
    <span class="nav-item" style="left:118px">Shop</span>
    <span class="nav-item" style="left:172px">Blog</span>
    <span class="nav-item" style="left:221px">Portfolio</span>
  </nav>
  <div class="abs search">Search...</div>
  <div class="abs submit">Submit</div>
</header>

<section class="abs slider">
  <div class="slide-photo" role="img" aria-label="Banner photo of a stone-grey tailored suit jacket"></div>
  <span class="arrow" style="left:13px;top:47px"><svg width="8" height="8"><path d="M6 0L2 4l4 4" fill="none" stroke="#fff" stroke-width="1.6"/></svg></span>
  <span class="arrow" style="left:730px;top:47px"><svg width="8" height="8"><path d="M2 0l4 4-4 4" fill="none" stroke="#fff" stroke-width="1.6"/></svg></span>
  <span class="dot" style="left:747px;top:5px"></span>
  <div class="slide-caption">Second Thumbnail label<br>Cras justo odio, dapibus ac facilisis in, egestas eget quam. Donec id elit non mi porta gravida at eget metus. Nullam id dolor id nibh ultricies vehicula ut id elit.</div>
</section>

<section class="abs hello">
  <h1>HELLO FOLKS! WE’RE THE BEST FASHION STORE.</h1>
  <p>We specialises in online trading between buyers and sellers of fashion apparel.</p>
  <span class="cta">Go To Shop Catalog</span>
</section>

<h2 class="abs section-title" style="top:360px;font-weight:400">
  <svg width="16" height="13" viewBox="0 0 16 13"><path d="M8 13L1.5 6.5A3.6 3.6 0 018 1.7a3.6 3.6 0 016.5 4.8z" fill="#000"/></svg>Latest Fashion
</h2>

<div class="abs card" style="left:58px;top:385px;height:209px">
  <div class="photo" role="img" aria-label="Charcoal suit jacket" style="height:100px;background:linear-gradient(var(--suit-grey),#555)"></div>
  <div class="card-title" style="margin-top:10px">Fashion Guys<span class="count"><svg width="14" height="12"><ellipse cx="7" cy="5" rx="6" ry="4.2" fill="none" stroke="#2f86d1" stroke-width="1.4"/><path d="M3 8l-1 3 3-2" fill="#2f86d1"/></svg>3</span></div>
  <div class="btn-detail" style="margin-top:10px">👁 View Detail</div>
  <div class="btn-cart">🛒 Add to Char $34</div>
  <div class="meta" style="margin-top:16px">▤ Clothiing, Bikini</div>
</div>
<div class="abs card" style="left:324px;top:385px;height:209px">
  <div class="photo" role="img" aria-label="Stone-grey suit jacket" style="height:100px;background:linear-gradient(#d0cbc0,var(--suit-stone))"></div>
  <div class="card-title" style="margin-top:10px">Fashion Guys<span class="count"><svg width="14" height="12"><ellipse cx="7" cy="5" rx="6" ry="4.2" fill="none" stroke="#2f86d1" stroke-width="1.4"/><path d="M3 8l-1 3 3-2" fill="#2f86d1"/></svg>3</span></div>
  <div class="btn-detail" style="margin-top:10px">👁 View Detail</div>
  <div class="btn-cart">🛒 Add to Char $34</div>
  <div class="meta" style="margin-top:16px">▤ Clothiing, Bikini</div>
</div>
<div class="abs card" style="left:591px;top:385px;height:209px">
  <div class="photo" role="img" aria-label="Checked blue jacket with scarf" style="height:100px;background:linear-gradient(#a9a29a,var(--suit-check))"></div>
  <div class="card-title" style="margin-top:10px">Fashion Guys<span class="count"><svg width="14" height="12"><ellipse cx="7" cy="5" rx="6" ry="4.2" fill="none" stroke="#2f86d1" stroke-width="1.4"/><path d="M3 8l-1 3 3-2" fill="#2f86d1"/></svg>3</span></div>
  <div class="btn-detail" style="margin-top:10px">👁 View Detail</div>
  <div class="btn-cart">🛒 Add to Char $34</div>
  <div class="meta" style="margin-top:16px">▤ Clothiing, Bikini</div>
</div>

<h2 class="abs section-title" style="top:606px;font-weight:400">
  <svg width="16" height="12" viewBox="0 0 16 12"><rect x="0" y="0" width="7" height="5" fill="#000"/><rect x="8" y="0" width="7" height="5" fill="#000"/><rect x="0" y="6" width="7" height="5" fill="#000"/><rect x="8" y="6" width="7" height="5" fill="#000"/></svg>Product Category
</h2>

<div class="abs tile" style="left:58px"><div class="photo" role="img" aria-label="Charcoal suit jacket" style="background:linear-gradient(var(--suit-grey),#555)"></div><div class="tile-label">Shop baju Cewek</div></div>
<div class="abs tile" style="left:258px"><div class="photo" role="img" aria-label="Stone-grey suit jacket" style="background:linear-gradient(#d0cbc0,var(--suit-stone))"></div><div class="tile-label">Shop baju Cewek</div></div>
<div class="abs tile" style="left:458px"><div class="photo" role="img" aria-label="Checked blue jacket with scarf" style="background:linear-gradient(#a9a29a,var(--suit-check))"></div><div class="tile-label">Shop baju Cewek</div></div>
<div class="abs tile" style="left:657px"><div class="photo" role="img" aria-label="Peach quilted jacket" style="background:linear-gradient(#f0d8c6,var(--suit-peach))"></div><div class="tile-label">Shop baju Cewek</div></div>
<div class="abs" style="left:0;top:706px;width:900px;height:1px;background:#9a9a9a"></div>
<span class="arrow abs" style="left:73px;top:676px"><svg width="8" height="8"><path d="M6 0L2 4l4 4" fill="none" stroke="#fff" stroke-width="1.6"/></svg></span>
<span class="arrow abs" style="left:790px;top:676px"><svg width="8" height="8"><path d="M2 0l4 4-4 4" fill="none" stroke="#fff" stroke-width="1.6"/></svg></span>

<h2 class="abs section-title" style="top:764px;font-weight:400">
  <svg width="16" height="12" viewBox="0 0 16 12"><path d="M1 4h4l8-4v12L5 8H1z" fill="#000"/></svg>Latest Blog
</h2>

<div class="abs card" style="left:58px;top:792px;height:227px">
  <div class="photo" role="img" aria-label="Peach quilted jacket" style="height:110px;background:linear-gradient(#f0d8c6,var(--suit-peach))"></div>
  <div class="card-title" style="margin-top:8px;justify-content:flex-start;gap:6px;padding-left:17px">News of Fashion<span class="count"><svg width="14" height="12"><ellipse cx="7" cy="5" rx="6" ry="4.2" fill="none" stroke="#2f86d1" stroke-width="1.4"/><path d="M3 8l-1 3 3-2" fill="#2f86d1"/></svg>3</span></div>
  <p class="blog-text" style="margin-top:14px">lorem ipsum do color lorm lorem ipsum do color lormlorem ipsum do color lorm lorem ipsum do color lorm</p>
  <p class="blog-meta" style="margin-top:19px">👤 Melvaroth, ▤ Format, 💬 4 Comment</p>
</div>
<div class="abs card" style="left:324px;top:792px;height:227px">
  <div class="photo" role="img" aria-label="Stone-grey suit jacket" style="height:110px;background:linear-gradient(#d0cbc0,var(--suit-stone))"></div>
  <div class="card-title" style="margin-top:8px;justify-content:flex-start;gap:6px;padding-left:17px">News of Fashion<span class="count"><svg width="14" height="12"><ellipse cx="7" cy="5" rx="6" ry="4.2" fill="none" stroke="#2f86d1" stroke-width="1.4"/><path d="M3 8l-1 3 3-2" fill="#2f86d1"/></svg>3</span></div>
  <p class="blog-text" style="margin-top:14px">lorem ipsum do color lorm lorem ipsum do color lormlorem ipsum do color lorm lorem ipsum do color lorm</p>
  <p class="blog-meta" style="margin-top:19px">👤 Melvaroth, ▤ Format, 💬 4 Comment</p>
</div>
<div class="abs card" style="left:590px;top:792px;height:227px">
  <div class="photo" role="img" aria-label="Checked blue jacket with scarf" style="height:110px;background:linear-gradient(#a9a29a,var(--suit-check))"></div>
  <div class="card-title" style="margin-top:8px;justify-content:flex-start;gap:6px;padding-left:17px">News of Fashion<span class="count"><svg width="14" height="12"><ellipse cx="7" cy="5" rx="6" ry="4.2" fill="none" stroke="#2f86d1" stroke-width="1.4"/><path d="M3 8l-1 3 3-2" fill="#2f86d1"/></svg>3</span></div>
  <p class="blog-text" style="margin-top:14px">lorem ipsum do color lorm lorem ipsum do color lormlorem ipsum do color lorm lorem ipsum do color lorm</p>
  <p class="blog-meta" style="margin-top:19px">👤 Melvaroth, ▤ Format, 💬 4 Comment</p>
</div>

<footer class="abs footer">
  <h2 style="left:60px">Bright Cove Hub (bch)</h2>
  <p class="about">Why don't we just give everybody a promotion and call it a night - 'Commander'? I am your worst nightmare! Maybe we better talk out here; the observation lounge has turned into a swamp. Flair is what marks the difference between artistry and mere competence. I can't. As much as I care about you, my first duty is to the ship. We finished our first sensor sweep of the neutral zone.</p>
  <h2 style="left:325px">Random Product</h2>
  <div class="random" style="top:42px">
    <div class="thumb" style="top:0"><div role="img" aria-label="Checked blue jacket with scarf" style="background:linear-gradient(#a9a29a,var(--suit-check))"></div></div>
    <span class="name" style="top:0">lorem ipsum do color</span>
    <span class="price" style="top:15px">$234</span>
    <div class="thumb" style="top:52px"><div role="img" aria-label="Peach quilted jacket" style="background:linear-gradient(#f0d8c6,var(--suit-peach))"></div></div>
    <span class="name" style="top:52px">lorem ipsum do color</span>
    <span class="price" style="top:67px">$234</span>
  </div>
  <h2 style="left:591px">Tags</h2>
  <div class="tags">
    <span class="tag">Shop</span><span class="tag">Shadsfasfop</span><span class="tag">Shafgsdgsop</span>
    <span class="tag">Sfafhop</span><span class="tag">Shoping</span><span class="tag">Shoasdp</span>
    <span class="tag">Shosfafap</span>
  </div>
</footer>

<div class="abs bottom-bar">Copyright © 2013 <span>Bright Cove Hub</span>
  <div class="social"><i></i><i></i><i></i><i></i></div>
</div>
</body>
</html>
```